Road Sign at our office 84 in X 48 in - Small Billboard

Kestrel Electrical
Electrical & Lighting Services

- we need a sign design for our small business/company based in Calhoun, GA called Kestrel Electrical - "our mission is to provide Northwest Georgia with dependable, high-quality electrical services that prioritize safety, integrity, and long-term reliability. As a woman-owned business with over 25 years of experience, we are committed to delivering exceptional workmanship and personalized service for every commercial, residential, and industrial project we undertake. We stand behind our work with a lifetime warranty—because your trust is our most powerful connection."

display logo, phone number, and open to other ideas without being cluttered, maybe instead of full website address, just use @kstelectrical and it will send them to all of our website and socials...

it needs to be easy to read as they drive down the road
this is a place where people may be traveling at high speeds, make sure it's easy to see and understand at a glance.
It will be hanging 20-24ft from the ground. Like a small billboard.

https://kstelectricalservices.example/

Industry/Entity Type

Electrical Contractor

Requirements
Nice to have
• match the look and feel of website and socials

```html
<!DOCTYPE html>
<html lang="en">
<head>
<meta charset="utf-8">
<title>Kestrel Electrical – Road Sign</title>
<link rel="stylesheet" href="https://fonts.googleapis.com/css2?family=Montserrat:wght@700&family=Arimo:wght@700&display=swap">
<style>
  :root {
    --backdrop: #9a9a9a;
    --sign-white: #ffffff;
    --ink: #141414;
    --flame-red: #e8542a;
    --flame-orange: #f7941d;
    --ember-brown: #8f2f12;
    --pill-top: #f9a24a;
    --pill-bottom: #e9661f;
  }
  * { margin: 0; padding: 0; box-sizing: border-box; }
  html, body {
    width: 1200px; height: 843px; overflow: hidden;
    background: var(--backdrop);
  }
  .sign {
    position: absolute; left: 40px; top: 101px;
    width: 1120px; height: 640px;
    background: var(--sign-white);
    overflow: hidden;
    box-shadow: 0 4px 14px rgba(0,0,0,.25);
  }
  .sign__swoosh { position: absolute; inset: 0; width: 100%; height: 100%; }
  .brand-mark {
    position: absolute; left: 43px; top: 160px;
    width: 200px; height: 200px; border-radius: 50%;
    background: var(--flame-orange);
  }
  .tagline {
    position: absolute; right: 47px; top: 28px;
    font-family: "Arimo", Arial, sans-serif; font-weight: 700;
    font-size: 64px; line-height: 66px; text-align: right;
  }
  .tagline__line { display: block; }
  .tagline__line--first { color: var(--flame-red); margin-right: 140px; }
  .tagline__line--second { color: var(--flame-orange); }
  .brand-name {
    position: absolute; left: 285px; top: 175px;
    font-family: "Montserrat", Arial, sans-serif; font-weight: 700;
    color: var(--ink);
  }
  .brand-name__main { display: block; font-size: 150px; line-height: 160px; letter-spacing: -2px; }
  .brand-name__sub { display: block; font-size: 56px; line-height: 64px; letter-spacing: 21px; margin-top: 2px; }
  .phone-pill {
    position: absolute; left: 490px; top: 432px;
    width: 588px; height: 90px; border-radius: 45px;
    background: linear-gradient(var(--pill-top), var(--pill-bottom));
    color: var(--sign-white);
    font-family: "Arimo", Arial, sans-serif; font-weight: 700;
    font-size: 70px; line-height: 90px; text-align: center;
  }
  .social-handle {
    position: absolute; left: 515px; top: 546px;
    width: 520px; text-align: center;
    color: var(--sign-white);
    font-family: "Arimo", Arial, sans-serif; font-weight: 700;
    font-size: 62px; line-height: 70px;
  }
</style>
</head>
<body>
  <main class="sign">
    <svg class="sign__swoosh" viewBox="0 0 1120 640" aria-hidden="true">
      <path d="M120 640 C 400 530, 760 490, 1120 492 L1120 640 Z" fill="var(--flame-orange)"/>
      <path d="M232 640 C 500 560, 800 525, 1120 522 L1120 640 Z" fill="var(--ember-brown)"/>
    </svg>

    <div class="brand-mark"></div>

    <p class="tagline">
      <span class="tagline__line tagline__line--first">ELECTRICAL</span>
      <span class="tagline__line tagline__line--second">&amp; LIGHTING</span>
    </p>

    <h1 class="brand-name">
      <span class="brand-name__main">Kestrel</span>
      <span class="brand-name__sub">ELECTRICAL</span>
    </h1>

    <p class="phone-pill">706-555-0142</p>
    <p class="social-handle">@kstelectrical</p>
  </main>
</body>
</html>
```